Willowmere Equine Sanctuary Flyer Urgent

Willowmere Equine Sanctuary

Rescue • Rehabilitation • Sanctuary

Willowmere Equine Sanctuary provides a safe and ethical refuge for horses, ponies and donkeys who have nowhere else to go. Some arrive needing rehabilitation and careful retraining, while others find permanent sanctuary here due to age, injury or behavioural needs.

Our mission is simple: to improve the physical and psychological wellbeing of every animal in our care.

At Willowmere we focus on:
• Rescue and rehabilitation of horses in need
• Lifetime sanctuary for those who cannot be rehomed
• Education and advocacy for responsible horse care
• Equine rehabilitation services to help horses recover and thrive

Sponsor a Horse

One of the most meaningful ways to support our work is by sponsoring one of our residents. Each horse, pony or donkey only has one sponsor!

Your sponsorship helps provide:
• Hay and feed
• Veterinary care
• Hoof trimming and routine health care
• Rugs, shelter and daily care

Many of our horses will live out their lives here, and sponsorship ensures they are safe, well fed and cared for every single day.

Sponsorship starts from $15 - $25 per week / $60 -$100 per month.

How You Can Help

• Sponsor a horse
• Make a donation
• Share our work with others

Your support helps us continue to say yes to horses who need a second chance.

📍 Willowmere Park, Victoria
📧 carla@willowmerepaddock.org

📞 0400 519 627

Font styles to use
Serif
Sans Serif

Colors
F0912C
F2A743
F7CA91
FBE8D2
FDF5EE
EE7325
F08F49
F5BC92
FAE3D3
FDF4ED

Requirements
Should not have
• Photos not provided by Willowmere

```html
<!DOCTYPE html>
<html lang="en">
<head>
<meta charset="utf-8">
<title>Willowmere Equine Sanctuary Flyer</title>
<link rel="stylesheet" href="https://fonts.googleapis.com/css2?family=Oswald:wght@300;400;500;600&family=Montserrat:wght@800&display=swap">
<style>
  :root{
    --orange:#f0862f;
    --orange-deep:#ee7325;
    --cream:#fdebdb;
    --cream-light:#fdf5ee;
    --red:#e5232b;
    --blue:#3d52a6;
    --ink:#141414;
    --grey:#6b6b6b;
    --white:#ffffff;
  }
  *{margin:0;padding:0;box-sizing:border-box}
  html,body{width:1200px;height:841px;overflow:hidden;background:var(--white)}
  body{position:relative;font-family:"Oswald",sans-serif}
  .page{position:absolute;overflow:hidden;background:var(--white);box-shadow:3px 4px 8px rgba(0,0,0,.18)}
  .page--sponsor{left:16px;top:18px;width:576px;height:814px}
  .page--about{left:611px;top:21px;width:565px;height:801px}
  .shape{position:absolute;left:0;top:0;width:100%;height:100%}
  .abs{position:absolute;z-index:2}

  /* sponsor page */
  .sponsor-title{left:256px;top:6px;width:306px;white-space:nowrap;font-size:44px;font-weight:500;color:var(--blue);line-height:66px;letter-spacing:-.6px;text-align:center}
  .sponsor-intro{left:240px;top:80px;width:328px;font-size:11.4px;font-weight:400;color:var(--grey);line-height:15.5px;text-align:center}
  .provide-head{left:243px;top:118px;white-space:nowrap;font-size:18px;font-weight:500;color:var(--red);line-height:24px}
  .provide-list{left:270px;top:146px;list-style:none;font-size:14.5px;font-weight:500;color:var(--ink);line-height:16.5px}
  .provide-list li{position:relative;margin-bottom:2.5px;width:160px}
  .provide-list li::before{content:"°";position:absolute;left:-9px;top:-4px;color:var(--red);font-weight:600}
  .price-badge{left:452px;top:126px;width:114px;height:126px;background:var(--blue);border-radius:50%;transform:rotate(-16deg);color:var(--white);text-align:center;padding-top:18px;line-height:15px}
  .price-badge .b1{font-size:14px;font-weight:600}
  .price-badge .b2{font-size:14px;font-weight:300}
  .price-badge .amt{font-size:17px;font-weight:600;color:var(--red)}
  .price-badge .b3{font-size:14px;font-weight:400}
  .sponsor-note{left:212px;top:243px;width:300px;font-size:11.4px;color:var(--grey);line-height:15.5px}
  .help-title{left:50px;top:312px;font-family:"Montserrat",sans-serif;font-weight:800;font-size:52px;line-height:55px;color:var(--red)}
  .help-list{left:251px;top:318px;list-style:none;font-size:26px;font-weight:500;color:var(--ink);line-height:48px;white-space:nowrap}
  .help-list li::before{content:"· ";font-weight:600}
  .help-cta{left:251px;top:462px;font-size:22.5px;font-weight:500;color:var(--red);line-height:32px;white-space:nowrap}
  .footer{left:0;top:772px;width:576px;height:42px;background:var(--orange);display:flex;align-items:center;padding-left:28px;gap:9px;color:var(--ink);font-size:15px;font-weight:500;white-space:nowrap}
  .footer .icon{width:13px;height:13px;flex:none}
  .footer .item{display:flex;align-items:center;gap:6px;margin-right:6px}
  .footer .phone{font-size:22px;font-weight:500}

  /* about page */
  .brand{left:335px;top:18px;width:215px;height:96px}
  .brand-name{position:absolute;right:62px;top:14px;text-align:right;color:var(--red);font-size:25px;font-weight:400;line-height:28px;white-space:nowrap}
  .brand-name span{display:block;font-size:15px;line-height:20px;margin-top:6px;border-top:1px solid var(--red);padding-top:4px}
  .brand-mark{position:absolute;right:0;top:0;width:54px;height:96px;background:var(--orange)}
  .about-title{left:15px;top:370px;font-size:47px;font-weight:600;color:var(--red);line-height:45px;letter-spacing:-1px;white-space:nowrap}
  .about-text{left:16px;top:522px;width:200px;font-size:11.8px;font-weight:300;color:var(--grey);line-height:14.2px}
  .mission{left:366px;top:296px;width:188px;height:230px;border-radius:50%;background:var(--blue);color:var(--white);text-align:center;padding:20px 10px 0}
  .mission h2{font-size:19px;font-weight:500;line-height:19px}
  .mission p{font-size:9.4px;font-weight:300;line-height:12px;margin:2px auto 0;width:122px}
  .mission hr{border:0;border-top:1px solid var(--red);width:130px;margin:7px auto 6px}
  .mission ul{list-style:none;font-size:7px;font-weight:300;line-height:12px;margin-top:5px}
  .mission li::before{content:"· "}
</style>
</head>
<body>

<section class="page page--sponsor">
  <svg class="shape" viewBox="0 0 576 814" aria-hidden="true">
    <rect x="0" y="0" width="576" height="814" fill="var(--white)"/>
    <polygon points="193,272 576,272 576,584 193,584" fill="var(--cream)"/>
    <polygon points="238,0 576,0 576,77 222,77" fill="var(--orange)"/>
    <polygon points="0,272 193,272 246,432 193,584 0,584" fill="var(--orange)"/>
  </svg>
  <svg class="shape" viewBox="0 0 576 814" role="img" aria-label="Photo of a small white pony wearing a flower crown in a green paddock">
    <defs><linearGradient id="g-pony" x1="0" y1="0" x2="0" y2="1"><stop offset="0" stop-color="#4a4f3c"/><stop offset=".6" stop-color="#8c9274"/><stop offset="1" stop-color="#6f8a47"/></linearGradient></defs>
    <polygon points="0,0 254,0 193,272 0,272" fill="url(#g-pony)"/>
  </svg>
  <svg class="shape" viewBox="0 0 576 814" role="img" aria-label="Photo of a herd of brown, black and white horses by a paddock fence">
    <defs><linearGradient id="g-herd" x1="0" y1="0" x2="0" y2="1"><stop offset="0" stop-color="#56663f"/><stop offset=".55" stop-color="#7a5a3e"/><stop offset="1" stop-color="#8f9a6a"/></linearGradient></defs>
    <rect x="0" y="584" width="576" height="188" fill="url(#g-herd)"/>
  </svg>

  <h1 class="abs sponsor-title">Sponsor a Horse</h1>
  <p class="abs sponsor-intro">One of the most meaningful ways to support our work is by sponsoring one of our residents. Each horse, pony or donkey only has one sponsor!</p>
  <h2 class="abs provide-head">Your sponsorship helps provide:</h2>
  <ul class="abs provide-list">
    <li>Hay and feed</li>
    <li>Veterinary care</li>
    <li>Hoof trimming and routine health care</li>
    <li>Rugs, shelter and daily care</li>
  </ul>
  <div class="abs price-badge">
    <div class="b1">Sponsorship</div>
    <div class="b2">starts from</div>
    <div class="amt">$15 - $25</div>
    <div class="b3">per week/</div>
    <div class="amt">$60 -$100</div>
    <div class="b3">per month.</div>
  </div>
  <p class="abs sponsor-note">Many of our horses will live out their lives here, and sponsorship ensures they are safe, well fed and cared for every single day.</p>

  <h2 class="abs help-title">How<br>You<br>Can<br>Help</h2>
  <ul class="abs help-list">
    <li>Sponsor a horse</li>
    <li>Make a donation</li>
    <li>Share our work with others</li>
  </ul>
  <p class="abs help-cta">Your support helps us continue<br>to say yes to horses who need<br>a second chance.</p>

  <footer class="abs footer">
    <span class="item">
      <svg class="icon" viewBox="0 0 14 14" aria-hidden="true"><circle cx="7" cy="7" r="7" fill="var(--red)"/><path d="M7 3.2a2.4 2.4 0 0 0-2.4 2.4C4.6 7.4 7 10.6 7 10.6s2.4-3.2 2.4-5A2.4 2.4 0 0 0 7 3.2z" fill="var(--white)"/><circle cx="7" cy="5.6" r=".9" fill="var(--red)"/></svg>
      Willowmere Park, Victoria
    </span>
    <span class="item">
      <svg class="icon" viewBox="0 0 14 14" aria-hidden="true"><circle cx="7" cy="7" r="7" fill="var(--red)"/><rect x="3.6" y="4.6" width="6.8" height="4.8" fill="none" stroke="var(--white)" stroke-width="1"/><path d="M3.6 4.6 7 7.4l3.4-2.8" fill="none" stroke="var(--white)" stroke-width="1"/></svg>
      carla@willowmerepaddock.org
    </span>
    <span class="item phone">
      <svg class="icon" viewBox="0 0 14 14" aria-hidden="true"><circle cx="7" cy="7" r="7" fill="var(--red)"/><path d="M4.6 3.8l1.3-.3.8 1.9-.9.7a5 5 0 0 0 2.1 2.1l.7-.9 1.9.8-.3 1.3c-3 .2-5.8-2.6-5.6-5.6z" fill="var(--white)"/></svg>
      0400 519 627
    </span>
  </footer>
</section>

<section class="page page--about">
  <svg class="shape" viewBox="0 0 565 801" role="img" aria-label="Photo of a fawn and a dog touching noses">
    <defs><linearGradient id="g-fawn" x1="0" y1="0" x2="1" y2="0"><stop offset="0" stop-color="#8c7a4e"/><stop offset=".6" stop-color="#6b4a2c"/><stop offset="1" stop-color="#3a3022"/></linearGradient></defs>
    <polygon points="13,0 307,0 347,147 51,147" fill="url(#g-fawn)"/>
  </svg>
  <svg class="shape" viewBox="0 0 565 801" role="img" aria-label="Photo of two brown horses nuzzling each other">
    <defs><linearGradient id="g-pair" x1="0" y1="0" x2="1" y2="1"><stop offset="0" stop-color="#b9b3a3"/><stop offset=".5" stop-color="#6b3f27"/><stop offset="1" stop-color="#3d2619"/></linearGradient></defs>
    <polygon points="91,159 387,159 440,410 165,410" fill="url(#g-pair)"/>
  </svg>
  <svg class="shape" viewBox="0 0 565 801" role="img" aria-label="Photo of a grey donkey wearing a cap beside a handler">
    <defs><linearGradient id="g-donkey" x1="0" y1="0" x2="1" y2="0"><stop offset="0" stop-color="#6d7457"/><stop offset=".5" stop-color="#9a9a96"/><stop offset="1" stop-color="#5f8ea6"/></linearGradient></defs>
    <polygon points="234,468 546,468 509,616 202,616" fill="url(#g-donkey)"/>
  </svg>
  <svg class="shape" viewBox="0 0 565 801" role="img" aria-label="Photo of a group of small ponies standing together">
    <defs><linearGradient id="g-ponies" x1="0" y1="0" x2="1" y2="0"><stop offset="0" stop-color="#3b2a20"/><stop offset=".6" stop-color="#7a5638"/><stop offset="1" stop-color="#c7b7a3"/></linearGradient></defs>
    <rect x="0" y="627" width="229" height="174" fill="url(#g-ponies)"/>
  </svg>
  <svg class="shape" viewBox="0 0 565 801" role="img" aria-label="Photo of a white goat and a deer in a paddock">
    <defs><linearGradient id="g-goat" x1="0" y1="0" x2="1" y2="1"><stop offset="0" stop-color="#6f7f52"/><stop offset=".6" stop-color="#c9c4b8"/><stop offset="1" stop-color="#4e5b39"/></linearGradient></defs>
    <polygon points="268,624 566,624 519,803 223,803" fill="url(#g-goat)"/>
  </svg>

  <div class="abs brand">
    <div class="brand-name">Willowmere<span>Equine Sanctuary</span></div>
    <div class="brand-mark" aria-hidden="true"></div>
  </div>

  <h1 class="abs about-title">Rescue<br>Rehabilitation<br>Sanctuary</h1>
  <p class="abs about-text">Willowmere Equine Sanctuary provides a safe and ethical refuge for horses, ponies and donkeys who have nowhere else to go. Some arrive needing rehabilitation and careful retraining, while others find permanent sanctuary here due to age, injury or behavioural needs.</p>

  <div class="abs mission">
    <h2>Our mission is<br>simple:</h2>
    <p>to improve the physical and psychological wellbeing of every animal in our care.</p>
    <hr>
    <h2>At Willowmere<br>we focus on:</h2>
    <ul>
      <li>Rescue and rehabilitation of horses in need</li>
      <li>Lifetime sanctuary for those who cannot be rehomed</li>
      <li>Education and advocacy for responsible horse care</li>
      <li>Equine rehabilitation services to help horses recover and thrive</li>
    </ul>
  </div>
</section>

</body>
</html>
```